Postcard needed for expert witness service

Looking for a professional postcard that will be mailed to personal injury lawyers / law firms to introduce my expert witness services.

Target Market(s)

Law firms, personal injury lawyers

Industry/Entity Type

Expert witness, law

Font styles to use
Sans Serif

Requirements
Must have
• Logo: The Frost Counsel [Main Heading]Do you handle snow and ice related slip and falls? Darrel is one of the top snow industry experts in the country! [Following should be in a list type fashion, possibly bulleted]Darrel's credentials: Accredited Winter Practitioner (AWP), past WRTA board member and chair, former ISO 9001 certified snow company owner , 32 years in the industry. (555) 284-3917 NOTES: Postcard will be 4" x 6" Please use both sides however must have room for labels and stamp
Should not have
• Wouldn't suggest using both photos on same side. Honestly, feel free to only use one of the slip and fall photos if it works out better. Thanks!

```html
<!DOCTYPE html>
<html lang="en">
<head>
<meta charset="utf-8">
<title>The Frost Counsel – Postcard</title>
<link href="https://fonts.googleapis.com/css2?family=Montserrat:wght@400;500;600;700&display=swap" rel="stylesheet">
<style>
  :root {
    --ink: #231f20;
    --accent: #3bbfe6;
    --paper: #ffffff;
    --page: #e9e7e4;
    --text: #1e1e1e;
    --rule: #2b2b2b;
  }
  * { box-sizing: border-box; margin: 0; padding: 0; }
  html, body { width: 1200px; height: 521px; overflow: hidden; }
  body {
    background: var(--page);
    font-family: "Montserrat", Arial, sans-serif;
    color: var(--text);
    position: relative;
  }
  .card {
    position: absolute;
    top: 51px;
    width: 552px;
    height: 368px;
    background: var(--paper);
    overflow: hidden;
    box-shadow: 0 2px 6px rgba(0,0,0,.25);
  }
  .card--front { left: 35px; }
  .card--back  { left: 613px; }

  /* FRONT */
  .hero-photo {
    position: absolute; left: 0; top: 0; width: 304px; height: 326px;
    background: linear-gradient(160deg, #9fb4cc 0%, #3f5a86 35%, #5a6878 65%, #8e949a 100%);
  }
  .headline-band {
    position: absolute; left: 0; top: 9px; width: 552px; height: 44px;
    background: var(--ink); text-align: center; padding-top: 4px;
  }
  .headline-band .question { color: var(--accent); font-size: 15.3px; font-weight: 500; line-height: 17px; }
  .headline-band .claim { color: #fff; font-size: 14.8px; font-weight: 500; line-height: 17px; }
  .credentials {
    position: absolute; left: 334px; top: 70px; width: 212px;
  }
  .credentials h2 { font-size: 11.8px; font-weight: 700; color: var(--ink); margin-bottom: 14px; letter-spacing: .1px; }
  .credentials ul { list-style: none; }
  .credentials li {
    position: relative; padding-left: 17px; font-size: 8.6px; line-height: 9.6px; margin-bottom: 5.4px;
  }
  .credentials li::before {
    content: ""; position: absolute; left: 2px; top: 1.5px; width: 6px; height: 6px;
    background: var(--accent); transform: rotate(45deg);
  }
  .inset-frame {
    position: absolute; left: 305px; top: 192px; width: 232px; height: 160px; background: var(--paper);
  }
  .inset-photo {
    position: absolute; left: 7px; top: 6px; width: 218px; height: 145px;
    background: linear-gradient(135deg, #8c8c8c 0%, #c7c7c7 40%, #5a463c 60%, #e6e6e6 100%);
  }
  .corner-shape { position: absolute; left: 403px; top: 297px; }
  .logo-tab { position: absolute; left: 0; top: 309px; }
  .brand {
    position: absolute; left: 19px; top: 329px; color: var(--ink);
    font-weight: 500; text-transform: uppercase; line-height: 1;
  }
  .brand .top { font-size: 16.5px; display: block; }
  .brand .bottom { font-size: 10.5px; letter-spacing: 3.2px; display: block; margin-top: 3px; }
  .front-phone {
    position: absolute; left: 158px; top: 337px; display: flex; align-items: center; gap: 5px;
    font-size: 13.4px; letter-spacing: .6px; color: var(--ink);
  }

  /* BACK */
  .frost-texture {
    position: absolute; left: 0; top: 60px; width: 260px; height: 308px;
    background: radial-gradient(ellipse at 20% 45%, #8f9599 0%, #c4c8cb 35%, rgba(255,255,255,0) 70%);
  }
  .back-brand {
    position: absolute; left: 32px; top: 24px; color: var(--ink); font-weight: 500; line-height: 1;
    text-transform: uppercase;
  }
  .back-brand .top { font-size: 18.5px; display: block; }
  .back-brand .bottom { font-size: 11px; letter-spacing: 3.6px; display: block; margin-top: 3px; }
  .intro {
    position: absolute; left: 32px; top: 115px; width: 148px;
    font-size: 6.5px; line-height: 10.4px; color: var(--text);
  }
  .call-shape { position: absolute; left: 0; top: 289px; }
  .call-block { position: absolute; left: 29px; top: 306px; }
  .call-block .cta { color: var(--accent); font-size: 14.6px; font-weight: 500; }
  .call-block .phone {
    display: flex; align-items: center; gap: 6px; color: #fff; font-size: 13.2px; margin-top: 4px;
  }
  .stamp-box {
    position: absolute; left: 424px; top: 40px; width: 91px; height: 117px; border: 1px solid var(--rule);
  }
  .address-line {
    position: absolute; left: 315px; width: 200px; border-top: 1px solid var(--rule);
  }
</style>
</head>
<body>

  <section class="card card--front">
    <div class="hero-photo" role="img" aria-label="Photo of a person slipping and falling on an icy sidewalk"></div>

    <header class="headline-band">
      <p class="question">Do you handle snow and ice related slip and falls?</p>
      <p class="claim">Darrel is one of the top snow industry experts in the country!</p>
    </header>

    <div class="credentials">
      <h2>DARREL'S CREDENTIALS:</h2>
      <ul>
        <li>Accredited Winter Practitioner (AWP),</li>
        <li>Past WRTA board member and chair,</li>
        <li>Former ISO 9001 certified snow company owner,</li>
        <li>32 years in the industry</li>
      </ul>
    </div>

    <svg class="corner-shape" width="149" height="71" viewBox="0 0 149 71">
      <polygon points="0,71 149,0 149,71" fill="var(--ink)"/>
    </svg>

    <div class="inset-frame">
      <div class="inset-photo" role="img" aria-label="Photo of a woman sitting after a fall on a snowy path"></div>
    </div>

    <svg class="logo-tab" width="145" height="59" viewBox="0 0 145 59">
      <polygon points="0,0 139,0 145,59 0,59" fill="var(--paper)"/>
    </svg>
    <div class="brand">
      <span class="top">The Frost</span>
      <span class="bottom">Counsel</span>
    </div>

    <div class="front-phone">
      <svg width="18" height="18" viewBox="0 0 24 24">
        <circle cx="12" cy="12" r="12" fill="var(--ink)"/>
        <path d="M8.6 6.2l1.6 2.6c.2.4.1.8-.2 1.1l-1 .8c.7 1.6 2 2.9 3.6 3.6l.8-1c.3-.3.7-.4 1.1-.2l2.6 1.6c.4.2.5.7.3 1.1l-.8 1.3c-.3.5-.9.7-1.4.6-3.7-.8-6.6-3.7-7.4-7.4-.1-.5.1-1.1.6-1.4l1.3-.8c.3-.2.8-.1.9.1z" fill="#fff"/>
      </svg>
      <span>(555) 284-3917</span>
    </div>
  </section>

  <section class="card card--back">
    <div class="frost-texture" role="img" aria-label="Frosted ice crystal texture fading into white"></div>

    <div class="back-brand">
      <span class="top">The Frost</span>
      <span class="bottom">Counsel</span>
    </div>

    <p class="intro">As an expert witness specializing in snow and ice management, I provide comprehensive insights and testimony to support your cases involving slip and fall incidents, snow removal disputes, and related claims. With extensive industry experience and a commitment to accuracy, I am ready to assist in building a solid foundation for your legal success.</p>

    <svg class="call-shape" width="205" height="79" viewBox="0 0 205 79">
      <polygon points="0,0 144,0 205,79 0,79" fill="var(--ink)"/>
    </svg>
    <div class="call-block">
      <p class="cta">Call me Today!</p>
      <p class="phone">
        <svg width="18" height="18" viewBox="0 0 24 24">
          <circle cx="12" cy="12" r="12" fill="var(--accent)"/>
          <path d="M8.6 6.2l1.6 2.6c.2.4.1.8-.2 1.1l-1 .8c.7 1.6 2 2.9 3.6 3.6l.8-1c.3-.3.7-.4 1.1-.2l2.6 1.6c.4.2.5.7.3 1.1l-.8 1.3c-.3.5-.9.7-1.4.6-3.7-.8-6.6-3.7-7.4-7.4-.1-.5.1-1.1.6-1.4l1.3-.8c.3-.2.8-.1.9.1z" fill="#fff"/>
        </svg>
        <span>(555) 284-3917</span>
      </p>
    </div>

    <div class="stamp-box"></div>
    <div class="address-line" style="top:227px"></div>
    <div class="address-line" style="top:260px"></div>
    <div class="address-line" style="top:294px"></div>
    <div class="address-line" style="top:328px"></div>
  </section>

</body>
</html>
```